Law Firm Marketing Postcard - Double Sided

6 x 11 two sided postcard. Templates attached. Two versions for back. Use either although the one with the entire bottom left blank is preferred.
Our company helps companies that are transitioning in their office space footprint, meaning they are changing where they work location -wise and/or the setup and layout. Reasons for change are generally due to - renovation, closures/expansion, acquisitions, mergers, closures, relocation or redesign. We are marketing to law firms in the NJ and Philadelphia-area.
Design we are looking for is where each side appeals differently. One side we want bold with our lime green popping against majority black background. One idea we had was maybe a page peeling or torn to reveal the green area with text. See attached as a rough visual. Certainly deviate to make it wow!
Second side - Should look more corporate to appeal to the law firm reader. We would like our service categories to be with a brief possibly with a brief description of the service or bulleted list descriptors. Up to designer to decide to or not to include description as we sometimes don't on other collateral. Required contact info and usage of the photos in some manner. This side should use our company colors but not overwhelm with the lime green.
We were also considering using, "Law Firms. Do you need to CYA..... Change Your Address?", in some way instead of the phrase - "Law Firm Plans 2024" which is on the draft attachment.

See attached files for reference materials and items to use. The Solutions Overview pdf contains alot of the info we would like included.
Pls include the text - "Consultants. Project Managers. Service Providers."
Ignore the ASSET MANAGEMENT service category that is on the Capability Statement attachment. It has been replaced with the Document Scanning etc service on the Solutions Overview pdf.
Even if rough design is provided that doesn't have every little thing listed, we can revise and tweak before final. Thanks immensely for your time!

Target Market(s)

Law Firms

Industry/Entity Type

Law

Colors
0054AA
0677BA
7BADD7
CADEEF
E8F1F8
59FF00
82FF00
B8FF75
E3FFCB
F4FFEA

Requirements
Must have
• See description
Nice to have
• See description

```html
<!DOCTYPE html>
<html lang="en">
<head>
<meta charset="utf-8">
<title>Corvale Postcard – Front and Back</title>
<link href="https://fonts.googleapis.com/css2?family=Bebas+Neue&family=Permanent+Marker&family=Montserrat:wght@500;600;700&family=Noto+Serif:wght@400;700&family=Source+Sans+3:wght@400;700&display=swap" rel="stylesheet">
<style>
  :root{
    --stage:#bcbec0;
    --ink:#000000;
    --lime:#7ed957;
    --lime-deep:#2f5a22;
    --white:#ffffff;
    --navy:#2b3f6b;
    --alert:#e3161b;
    --mail:#dce6f1;
    --text-dark:#222222;
  }
  *{box-sizing:border-box;margin:0;padding:0}
  html,body{width:1043px;height:1200px;overflow:hidden}
  body{background:var(--stage);position:relative;font-family:"Montserrat",sans-serif}

  .card{position:absolute;left:111px;width:820px;overflow:hidden;box-shadow:0 14px 12px -8px rgba(0,0,0,.28)}
  .card--front{top:101px;height:447px;background:var(--ink)}
  .card--back{top:623px;height:448px;background:var(--white)}

  /* ---------- front ---------- */
  .front-art{position:absolute;inset:0}
  .brand{position:absolute;left:26px;top:44px;width:196px;text-align:center;color:var(--navy)}
  .brand__name{font-family:"Montserrat",sans-serif;font-weight:700;font-size:40px;line-height:1;letter-spacing:-0.5px;display:block}
  .brand__tag{font-family:"Montserrat",sans-serif;font-weight:700;font-size:9.5px;letter-spacing:0.6px;display:block;margin-top:6px;color:var(--navy)}

  .headline{position:absolute;left:27px;line-height:1;white-space:nowrap}
  .headline--lead{top:146px;font-family:"Bebas Neue",sans-serif;font-size:104px;color:var(--lime);letter-spacing:-1px}
  .headline--plans{top:230px;font-family:"Bebas Neue",sans-serif;font-size:100px;color:var(--white);letter-spacing:-1px}
  .headline--year{top:308px;left:26px;font-family:"Permanent Marker","Bebas Neue",sans-serif;font-size:100px;color:var(--lime);letter-spacing:-2px}

  .services{position:absolute;left:424px;top:171px;list-style:none}
  .services li{position:relative;padding-left:16px;height:28.5px;color:var(--white);font-weight:600;font-size:19px;line-height:24px}
  .services li::before{content:"";position:absolute;left:0;top:5px;border-left:9px solid var(--white);border-top:7px solid transparent;border-bottom:7px solid transparent}

  .web-pill{position:absolute;top:398px;width:197px;height:28px;background:var(--ink);border-radius:14px;color:var(--white);font-family:"Noto Serif",serif;font-size:13.5px;line-height:28px;padding-left:36px;letter-spacing:0.4px}
  .web-pill--one{left:401px}
  .web-pill--two{left:606px}
  .web-pill__icon{position:absolute;left:-1px;top:-2px;width:32px;height:32px;border-radius:50%;background:var(--ink);border:2px solid var(--lime);display:flex;align-items:center;justify-content:center}

  /* ---------- back ---------- */
  .back-panel{position:absolute;left:0;top:0;width:820px;height:283px;background:var(--ink)}
  .service{position:absolute}
  .service__title{color:var(--lime);font-weight:700;font-size:18px;line-height:20px;letter-spacing:0.2px}
  .service__text{color:var(--white);font-weight:500;font-size:10.6px;line-height:14px;margin-top:6px}
  .service--space{left:97px;top:22px;width:190px}
  .service--move{left:97px;top:140px;width:195px}
  .service--move .service__text{margin-top:8px}
  .service--decom{left:590px;top:22px;width:210px}
  .service--decom .service__text{margin-top:13px}
  .service--furn{left:590px;top:140px;width:210px}
  .service--furn .service__text{margin-top:8px}

  .service-icon{position:absolute;background:var(--lime-deep);border-radius:6px}
  .service-icon--space{left:28px;top:37px;width:48px;height:61px}
  .service-icon--move{left:28px;top:163px;width:46px;height:62px}
  .service-icon--decom{left:516px;top:37px;width:62px;height:62px}
  .service-icon--furn{left:514px;top:165px;width:68px;height:66px}

  .photo{position:absolute;left:302px;width:192px;border:2px solid var(--lime)}
  .photo--interior{top:20px;height:119px;background:linear-gradient(180deg,#e9e9e7 0%,#b9bbbb 55%,#a88e72 100%)}
  .photo--empty{top:147px;height:123px;background:linear-gradient(180deg,#e4e6e8 0%,#9aa1a7 55%,#6f767c 100%)}

  .print-note{position:absolute;left:0;top:283px;width:529px;height:165px;text-align:center;padding-top:48px;font-family:"Source Sans 3",sans-serif;font-weight:700}
  .print-note__warn{color:var(--alert);font-size:17.5px;line-height:20px}
  .print-note__hint{color:var(--text-dark);font-size:17.5px;line-height:20px;margin-top:5px}
  .mail-area{position:absolute;left:529px;top:283px;width:291px;height:165px;background:var(--mail);text-align:center;padding-top:47px;font-family:"Source Sans 3",sans-serif;color:var(--text-dark);font-size:18.5px;line-height:23.5px}
</style>
</head>
<body>

<!-- FRONT -->
<section class="card card--front" aria-label="Postcard front">
  <svg class="front-art" width="820" height="447" viewBox="0 0 820 447">
    <defs>
      <linearGradient id="officeTone" x1="0" y1="0" x2="1" y2="1">
        <stop offset="0" stop-color="#d9dcde"/>
        <stop offset="0.6" stop-color="#8f979c"/>
        <stop offset="1" stop-color="#4b5358"/>
      </linearGradient>
      <linearGradient id="chairTone" x1="0" y1="0" x2="1" y2="1">
        <stop offset="0" stop-color="#b49a7a"/>
        <stop offset="0.45" stop-color="#6f7477"/>
        <stop offset="1" stop-color="#2e3236"/>
      </linearGradient>
    </defs>
    <polygon class="torn-edge" fill="#ffffff" points="372,0 380,12 370,25 378,40 368,58 376,72 366,90 374,108 364,125 372,140 362,160 370,178 360,195 368,212 358,230 366,248 356,265 364,282 356,300 362,318 354,335 362,352 354,370 360,388 352,405 360,420 354,435 360,447 820,447 820,0"/>
    <polygon class="green-field" fill="#7ed957" points="382,0 389,14 380,28 387,42 378,60 385,74 376,92 383,110 374,127 381,142 372,162 379,180 370,197 377,214 368,232 375,250 366,267 373,284 366,302 371,320 364,337 371,354 364,372 369,390 362,407 369,422 364,437 368,447 820,447 820,0"/>
    <polygon role="img" aria-label="Photo: wide open-plan office interior with architectural line drawing overlay" fill="url(#officeTone)" stroke="#ffffff" stroke-width="3" points="384,0 692,0 613,138 433,158 384,115"/>
    <polygon role="img" aria-label="Photo: office chair wrapped in plastic beside moving boxes" fill="url(#chairTone)" stroke="#ffffff" stroke-width="3" points="698,0 822,0 822,225 709,327 625,138"/>
  </svg>

  <div class="brand">
    <span class="brand__name">corvale</span>
    <span class="brand__tag">WORKPLACE SOLUTIONS</span>
  </div>

  <h1>
    <span class="headline headline--lead">LAW FRIM</span>
    <span class="headline headline--plans">PLANS</span>
    <span class="headline headline--year">2024?</span>
  </h1>

  <ul class="services">
    <li>Relocation</li>
    <li>Renovation</li>
    <li>Closure</li>
    <li>New Office</li>
    <li>Redesign</li>
    <li>Merger &amp; Acquisition</li>
    <li>Hybrid &amp; Hoteling</li>
  </ul>

  <div class="web-pill web-pill--one">
    <span class="web-pill__icon"><svg width="16" height="12" viewBox="0 0 16 12"><rect x="1" y="1" width="14" height="10" rx="1.5" fill="none" stroke="#7ed957" stroke-width="1.4"/><path d="M1.5 2 L8 7 L14.5 2" fill="none" stroke="#7ed957" stroke-width="1.4"/></svg></span>
    www.corvalews.com
  </div>
  <div class="web-pill web-pill--two">
    <span class="web-pill__icon"><svg width="16" height="12" viewBox="0 0 16 12"><rect x="1" y="1" width="14" height="10" rx="1.5" fill="none" stroke="#7ed957" stroke-width="1.4"/><path d="M1.5 2 L8 7 L14.5 2" fill="none" stroke="#7ed957" stroke-width="1.4"/></svg></span>
    www.corvalews.com
  </div>
</section>

<!-- BACK -->
<section class="card card--back" aria-label="Postcard back">
  <div class="back-panel">

    <div class="service-icon service-icon--space" role="img" aria-label="Icon: space planning"></div>
    <div class="service service--space">
      <h2 class="service__title">SPACE PLANING<br>&amp; DESIGN</h2>
      <p class="service__text">Planning and design to create healthy spaces according to desired function, flow, look, and feel</p>
    </div>

    <div class="service-icon service-icon--move" role="img" aria-label="Icon: move management"></div>
    <div class="service service--move">
      <h2 class="service__title">MOVE<br>MANAGEMENT</h2>
      <p class="service__text">Planning and Project Management of Moves/Adds/Changes, Re-stacks, and Reconfigurations with focused execution to decrease downtime and excessive costs.</p>
    </div>

    <div class="photo photo--interior" role="img" aria-label="Photo: modern glass-walled office with conference area"></div>
    <div class="photo photo--empty" role="img" aria-label="Photo: empty open office floor with column"></div>

    <div class="service-icon service-icon--decom" role="img" aria-label="Icon: decommissioning"></div>
    <div class="service service--decom">
      <h2 class="service__title">DECOMMISSION</h2>
      <p class="service__text">Plan, coordinate, manage, and execute all phases for decommissioning of facility, warehouse, office space, and assets (IT included - Servers, Cabling, E-waste).</p>
    </div>

    <div class="service-icon service-icon--furn" role="img" aria-label="Icon: furniture services"></div>
    <div class="service service--furn">
      <h2 class="service__title">FURNITURE<br>SERVICES</h2>
      <p class="service__text">Furniture procurement (purchase and leasing), delivery, receipt, dis/assembly, and installation. Surplus handling - liquidation, recycling, donation, and disposal. Refurbishment and repair</p>
    </div>
  </div>

  <div class="print-note">
    <p class="print-note__warn">You MUST remove this instruction layer or it will<br>be printed.</p>
    <p class="print-note__hint">(Turn off this layer in the “Layers” pallette)</p>
  </div>

  <div class="mail-area">
    <p>MAILING ADDRESS AREA<br>LEFT EMPTY<br>4.0 X 2.25</p>
  </div>
</section>

</body>
</html>
```